Single brochure for international companies in the financial sector

We need to update a brochure 4 pages presenting our company. We are a financial engineering company. The final design must provide financial security, service and trust. you will find the current brochure copy. Our color code is Orange (RGB 235/100/68), Black, White and Gray. photos show the visual of the site, but it is not mandatory to keep them.

Target Market(s)

wealth management professionals

Industry/Entity Type

Finance

Requirements
Must have
• Logo Tolvane Capital all text in the document color Orange Tolvane (RGB 235/100/68)
Nice to have
• Vista Font
Should not have
• images / pictures of people

```html
<!DOCTYPE html>
<html lang="en">
<head>
<meta charset="utf-8">
<title>Tolvane Capital – Brochure Spread</title>
<link rel="stylesheet" href="https://fonts.googleapis.com/css2?family=Jost:ital,wght@0,400;0,500;1,600&display=swap">
<style>
  :root {
    --orange: #eb6444;
    --orange-soft: #f3a58c;
    --black: #111111;
    --gray-text: #6b6b6b;
    --gray-bg: #bbbcbe;
    --paper: #ffffff;
    --rule: #f0b8a6;
  }
  * { box-sizing: border-box; margin: 0; padding: 0; }
  html, body { width: 1200px; height: 807px; overflow: hidden; }
  body {
    background: var(--gray-bg);
    font-family: "Jost", "Futura", sans-serif;
    position: relative;
  }
  .spread {
    position: absolute;
    left: 62px; top: 58px;
    width: 1078px; height: 699px;
    background:
      linear-gradient(90deg, rgba(0,0,0,0) 47%, rgba(0,0,0,0.035) 49.6%, rgba(0,0,0,0) 50.2%),
      radial-gradient(ellipse at 50% 0%, rgba(235,100,68,0.07), rgba(235,100,68,0) 45%),
      radial-gradient(ellipse at 50% 100%, rgba(235,100,68,0.06), rgba(235,100,68,0) 45%),
      var(--paper);
    box-shadow: 0 0 2px rgba(0,0,0,0.15);
  }
  .page-fold {
    position: absolute; left: 538px; top: 0; width: 1px; height: 100%;
    background: rgba(0,0,0,0.04);
  }
  .photo { position: absolute; }
  .photo--boardwalk {
    left: 12px; top: 1px; width: 166px; height: 363px;
    background: linear-gradient(180deg, #d98a74 0%, #f1c3b3 18%, #b9a79f 35%, #9c8f88 65%, #e2a793 100%);
  }
  .photo--arch {
    left: 888px; top: 334px; width: 166px; height: 365px;
    background: linear-gradient(135deg, #8a7f7a 0%, #5b4f4b 35%, #d9826a 60%, #f1a487 100%);
  }
  .tagline {
    position: absolute; left: 32px; top: 396px; width: 160px;
    color: var(--orange);
    font-weight: 600; font-style: italic;
    font-size: 14px; line-height: 18px;
  }
  .tagline p + p { margin-top: 18px; }
  .website {
    position: absolute; left: 32px; top: 667px;
    font-size: 12px; color: var(--gray-text);
  }
  .page-title {
    position: absolute;
    color: var(--orange);
    font-weight: 400; font-size: 21px; letter-spacing: 0.2px;
    padding-bottom: 8px;
  }
  .page-title::after {
    content: ""; position: absolute; left: 0; bottom: 0;
    width: 240px; height: 1px;
    background: linear-gradient(90deg, var(--orange-soft), rgba(240,184,166,0));
  }
  .page-title--company { left: 230px; top: 99px; }
  .page-title--services { left: 760px; top: 99px; }
  .section { position: absolute; }
  .section h2 {
    font-weight: 400; font-size: 17px; color: var(--black);
    margin-bottom: 6px;
  }
  .section p {
    font-size: 14px; line-height: 17px; color: var(--gray-text);
  }
  .section p.gap { margin-top: 17px; }
  .section .highlight { color: var(--orange); }
  .s-about   { left: 230px; top: 168px; width: 280px; }
  .s-clients { left: 230px; top: 326px; width: 280px; }
  .s-what    { left: 230px; top: 494px; width: 280px; }
  .s-advice  { left: 585px; top: 168px; width: 410px; }
  .s-analysis{ left: 585px; top: 326px; width: 290px; }
  .s-partner { left: 585px; top: 525px; width: 290px; }
</style>
</head>
<body>
  <div class="spread">
    <div class="page-fold"></div>

    <div class="photo photo--boardwalk" role="img" aria-label="Wooden boardwalk leading through dunes to the sea, orange-tinted photograph"></div>

    <div class="tagline">
      <p>Our Clients must deliver performance on their portfolios on a regular basis.</p>
      <p>We help them deliver everyday.</p>
    </div>

    <div class="website">www.tolvanecapital.com</div>

    <h1 class="page-title page-title--company">THE COMPANY</h1>

    <section class="section s-about">
      <h2>About Us</h2>
      <p>Tolvane Capital is a financial engineering company.</p>
      <p class="gap">It is fully independent from any bank or any other company.</p>
    </section>

    <section class="section s-clients">
      <h2>Clients</h2>
      <p>Our clients are financial professionals such as asset managers, institutionnals, corporates, private banks, wealth managers and family offices.<br>Our purpose is to make their work easier, every day.</p>
    </section>

    <section class="section s-what">
      <h2>What We Do</h2>
      <p>We provide them with investment solutions designed to improve their portfolios performance.<br><span class="highlight">Simple as that.</span></p>
    </section>

    <h1 class="page-title page-title--services">OUR SERVICES</h1>

    <section class="section s-advice">
      <h2>Investment Advice</h2>
      <p>Each client is looking for a unique investment solution. Hence, we combine internal and external resources to create the financial product that will best fit our clients requirements.<br>Thanks to a truly independent advice, we offer bespoke, simple and efficient solutions.</p>
    </section>

    <section class="section s-analysis">
      <h2>Portfolio Analysis</h2>
      <p>We advise our clients on their portfolios of financial products. Together we identify the needs for restructuring or reallocating the assets.</p>
      <p class="gap">We also provide full monitoring and reporting services throughout the life of the products.</p>
    </section>

    <section class="section s-partner">
      <h2>Partner Selection</h2>
      <p>Our internal tools allow us to continuously assess the issuers we are working with. Therefore we give our clients the luxury to chose among the best issuers for their investment solution.</p>
    </section>

    <div class="photo photo--arch" role="img" aria-label="Stone arch of an old viaduct seen from below against an orange sky"></div>
  </div>
</body>
</html>
```